International freight forwarder experienced in perishable handling needs a web design

We need a website designed that will allow us to capture more customers through the website. We would like a visually appealing design that is not so heavy on text. Our business covers the logistics and freight forwarding industries and we have offices in South America and the USA. Our main customers are importers USA, Europe, Asia and Russia and we currently work almost exclusively with perishable products such as fresh cut flowers, fresh exotics fruits, cacao, fresh fish etc. We would like to convey a fresh, modern approach to freight forwarding focusing on concepts such as - time sensitive, anytime-anywhere delivery, innovation, experience, reliability and confidence. Should include links with Chatterpost and Workvine. Our core solutions include: Core Services
*Air Freight
*Ocean Freight
*Warehousing & Distribution
Our industry solutions cover
*Flowers
*FMCG including, fruits, vegetables
*Live animals
*Automotive
*Consumer Goods
*Industrial
*Oil & Gas
*Pharma
* Event logistics
* Project logistics

Target Market(s)

Importers in Europe, USA, Asia, Middle East and Russia

Number of Pages Required

4 page

Font styles to use
Sans Serif

Colors
a1cd39
606060
000000

Requirements
Must have
• Photos of fresh cut flowers, FMCG such as cacao, fresh fish (packaged for shipping), fresh exotic fruits, pharma products (packaged for shipping), oil and gas etc. Internal customer login access
Nice to have
• Photos of cargo shipping carriers and cargo airline carriers. Features similar to those of following website http://www.vantoshipping.example/eng/main/index.jsp?FromURL=web
Should not have
• Too much text, needs to be visually pleasing

```html
<!DOCTYPE html>
<html lang="en">
<head>
<meta charset="utf-8">
<title>Freightora Alliance Group</title>
<link href="https://fonts.googleapis.com/css2?family=Oswald:wght@300;400;500&family=PT+Sans:wght@400;700&display=swap" rel="stylesheet">
<style>
:root{
  --green:#a1cd39;
  --green-dark:#7aa22a;
  --grey:#606060;
  --black:#000000;
  --header-top:#3a3a3a;
  --header-bottom:#1e1e1e;
  --footer:#232323;
  --text:#3c3c3c;
  --muted:#b4b4b4;
  --line:#d6d6d6;
  --page:#e4e4e4;
}
*{margin:0;padding:0;box-sizing:border-box}
html,body{width:1200px;height:1026px;overflow:hidden}
body{position:relative;background:var(--page);font-family:"PT Sans",Arial,sans-serif;color:var(--text)}
a{color:inherit;text-decoration:none}
.abs{position:absolute}

/* header */
.site-header{position:absolute;left:0;top:0;width:1200px;height:117px;background:linear-gradient(var(--header-top),var(--header-bottom))}
.brand{position:absolute;left:112px;top:30px;display:flex;align-items:center;gap:14px}
.brand-mark{width:54px;height:54px;border-radius:50%;background:var(--green)}
.brand-name{font-family:"PT Sans",sans-serif;font-weight:700;font-size:33px;color:#fff;letter-spacing:-.5px}
.call{position:absolute;left:705px;top:20px;font-family:"Oswald",sans-serif;font-size:20px;color:#fff}
.call span{color:var(--green)}
.btn-small{position:absolute;top:21px;height:27px;border-radius:3px;font-family:"PT Sans",sans-serif;font-weight:700;font-size:13px;display:flex;align-items:center;justify-content:center}
.btn-login{left:938px;width:69px;background:linear-gradient(#fff,#cfcfcf);color:#222}
.btn-signup{left:1015px;width:75px;background:linear-gradient(#b5db55,#86ad2c);color:#fff}
.main-nav{position:absolute;left:590px;top:67px;display:flex;align-items:center;font-family:"Oswald",sans-serif;font-weight:300;font-size:16px;color:#fff}
.main-nav a{padding:0 26px;border-left:1px solid #fff;line-height:20px}
.main-nav a:nth-child(2){border-left:none}
.main-nav .active{background:var(--green);padding:3px 14px;border-radius:2px;border:none;margin-right:8px}
.main-nav a:last-child{padding-right:0}

/* hero */
.hero{position:absolute;left:0;top:117px;width:1200px;height:319px;background:radial-gradient(ellipse at 45% 30%,#a6cf3a 0%,#8dbb2f 45%,#5f8a1e 100%)}
.hero-person{left:130px;top:38px;width:268px;height:281px;border-radius:6px 6px 0 0;background:linear-gradient(160deg,#d9c39a 0%,#3a6fc4 55%,#1d4f9e 100%)}
.hero-cargo{left:405px;top:52px;width:280px;height:230px;border-radius:8px;background:linear-gradient(150deg,#e9f0f6 0%,#5f9fd8 40%,#2850a8 70%,#c8a87a 100%);opacity:.9}
.hero-tag{left:706px;top:52px;font-family:"Oswald",sans-serif;font-weight:400;font-size:33px;color:#fff}
.hero-title{left:706px;top:96px;font-family:"Oswald",sans-serif;font-weight:400;font-size:57px;line-height:52px;color:#fff;letter-spacing:-.5px}
.btn-quote{left:710px;top:218px;width:184px;height:42px;border-radius:3px;background:linear-gradient(#fff,#d6d6d6);box-shadow:0 2px 3px rgba(0,0,0,.35);font-family:"PT Sans",sans-serif;font-weight:700;font-size:18px;color:#333;display:flex;align-items:center;justify-content:center}

/* services strip */
.services{position:absolute;left:0;top:436px;width:1200px;height:115px;background:linear-gradient(#e2e2e2,#fafafa);box-shadow:0 2px 3px rgba(0,0,0,.15)}
.service{position:absolute;top:0;height:115px;border-left:1px solid #c4c4c4}
.service:last-child{border-right:1px solid #c4c4c4}
.service-img{position:absolute;top:14px;height:88px;border-radius:3px}
.service h3{position:absolute;top:16px;font-family:"Oswald",sans-serif;font-weight:400;font-size:23px;color:#333;white-space:nowrap}
.service p{position:absolute;top:50px;width:170px;font-size:13px;line-height:16px;color:#777}
.service .more{position:absolute;top:84px;font-size:13px;font-weight:700;color:var(--green-dark)}

/* content panel */
.panel{position:absolute;left:92px;top:585px;width:1018px;height:326px;background:linear-gradient(#fff,#f3f3f3);border-radius:4px 4px 0 0;box-shadow:0 0 6px rgba(0,0,0,.12)}
.col-title{position:absolute;top:20px;font-family:"Oswald",sans-serif;font-weight:400;font-size:17px;color:#444}
.photo-frame{position:absolute;top:48px;width:300px;height:140px;border:1px solid #ddd;padding:4px;background:#fff}
.photo{width:100%;height:100%}
.col-text{position:absolute;width:300px;font-size:13px;line-height:20px;color:#444}
.cat{position:absolute;left:24px;top:196px;font-family:"Oswald",sans-serif;font-weight:400;font-size:17px;color:var(--green-dark)}
.arrows{position:absolute;left:291px;top:23px;display:flex;gap:2px}
.arrows span{width:14px;height:14px;display:block}
.news{position:absolute;left:698px;width:300px}
.news-item{position:absolute;left:0;width:300px;border-bottom:1px solid #e0e0e0;height:83px}
.news-item:last-child{border-bottom:none}
.news-date{font-size:11px;color:var(--muted);margin-top:5px}
.news-item p{font-size:13px;line-height:20px;color:#444;margin-top:4px}
.news-item a{color:var(--green-dark);font-weight:700}

/* footer */
.site-footer{position:absolute;left:0;top:911px;width:1200px;height:115px;background:var(--footer)}
.foot-nav{position:absolute;left:112px;top:33px;font-size:13px;color:#fff}
.foot-nav span{color:#aaa;margin:0 10px}
.copyright{position:absolute;left:113px;top:74px;font-size:13px;color:#999}
.follow{position:absolute;left:790px;top:32px;font-weight:700;font-size:14px;color:#fff}
.social{position:absolute;left:790px;top:61px;display:flex;gap:6px}
.social a{width:26px;height:26px;border-radius:50%;background:#9a9a9a;display:block}
.foot-brand{position:absolute;left:956px;top:24px;display:flex;flex-direction:column;align-items:center;gap:6px}
.foot-brand .dot{width:34px;height:34px;border-radius:50%;background:#777}
.foot-brand span{font-weight:700;font-size:20px;color:#9a9a9a;white-space:nowrap}
</style>
</head>
<body>

<header class="site-header">
  <a class="brand" href="#"><span class="brand-mark"></span><span class="brand-name">Freightora Alliance</span></a>
  <div class="call"><span>Call Us On:</span> +852 5550 0142</div>
  <a class="btn-small btn-login" href="#">LOGIN</a>
  <a class="btn-small btn-signup" href="#">SIGN UP</a>
  <nav class="main-nav">
    <a class="active" href="#">HOME</a>
    <a href="#">OUR SERVICES</a>
    <a href="#">INDUSTRY SOLUTIONS</a>
    <a href="#">CONTACT US</a>
  </nav>
</header>

<section class="hero">
  <div class="abs hero-person" role="img" aria-label="Smiling courier in blue uniform carrying a cardboard box"></div>
  <div class="abs hero-cargo" role="img" aria-label="Cargo plane, globe, container truck and forklift with boxes"></div>
  <div class="abs hero-tag">Fast &amp; Accurate Delivery</div>
  <h1 class="abs hero-title">FREIGHTORA ALLIANCE<br>GROUP</h1>
  <a class="abs btn-quote" href="#">GET QUOTES NOW</a>
</section>

<section class="services">
  <div class="service" style="left:110px;width:326px">
    <div class="service-img" role="img" aria-label="Open red shipping container with cartons" style="left:2px;width:126px;background:linear-gradient(90deg,#8e2a22,#c9a46e)"></div>
    <h3 style="left:142px">Ocean Freight</h3>
    <p style="left:142px">Lorem ipsum dolor sit amet consectetur adipiscing elit sed</p>
    <a class="more" style="left:143px" href="#">Read More...</a>
  </div>
  <div class="service" style="left:435px;width:329px">
    <div class="service-img" role="img" aria-label="Cargo airliner in flight" style="left:2px;width:126px;background:linear-gradient(90deg,#d8dde2,#8c959e)"></div>
    <h3 style="left:146px">Air Freight</h3>
    <p style="left:146px">Lorem ipsum dolor sit amet consectetur adipiscing elit sed</p>
    <a class="more" style="left:147px" href="#">Read More...</a>
  </div>
  <div class="service" style="left:763px;width:327px">
    <div class="service-img" role="img" aria-label="White delivery truck with trailer" style="left:2px;width:126px;background:linear-gradient(90deg,#eef0f2,#a9b0b6)"></div>
    <h3 style="left:142px">Warehousing &amp; ...</h3>
    <p style="left:143px">Lorem ipsum dolor sit amet consectetur adipiscing elit sed</p>
    <a class="more" style="left:144px" href="#">Read More...</a>
  </div>
</section>

<main class="panel">
  <h2 class="col-title" style="left:24px">INDUSTRY SOLUTIONS</h2>
  <div class="arrows">
    <svg width="14" height="14" viewBox="0 0 14 14"><rect width="14" height="14" fill="#aaa"/><path d="M8.5 4 5.5 7l3 3" stroke="#fff" stroke-width="1.5" fill="none"/></svg>
    <svg width="14" height="14" viewBox="0 0 14 14"><rect width="14" height="14" fill="#7aa22a"/><path d="M5.5 4l3 3-3 3" stroke="#fff" stroke-width="1.5" fill="none"/></svg>
  </div>
  <div class="photo-frame" style="left:24px"><div class="photo" role="img" aria-label="Red truck at a warehouse loading dock" style="background:linear-gradient(180deg,#c9ccd0 0%,#e6e7e9 45%,#c42a22 60%,#b9b9b9 100%)"></div></div>
  <h3 class="cat">INDUSTRIAL</h3>
  <p class="col-text" style="left:24px;top:220px">Lorem ipsum dolor sit amet, consectetur adipiscing elit sed do eiusmod tempor incididunt ut laborae et dolore exercitation ullamco laboris nisi ut aliquip.</p>

  <h2 class="col-title" style="left:351px">LATEST FROM THE BLOG</h2>
  <div class="photo-frame" style="left:351px"><div class="photo" role="img" aria-label="Palletised cargo being loaded beside a cargo aircraft" style="background:linear-gradient(180deg,#5f9ad8 0%,#c6dcf0 40%,#b78c63 70%,#7d7d7d 100%)"></div></div>
  <p class="col-text" style="left:352px;top:200px">Lorem ipsum dolor sit amet, consectetur adipiscing elit sed do eiusmod tempor incididunt ut laborae et dolore magna aliqua. Ut enim ad minim veniam, qauis nostrud exercitation ullamco laboris commodo.</p>

  <h2 class="col-title" style="left:698px">NEWS AND EVENT</h2>
  <div class="news" style="top:47px">
    <div class="news-item" style="top:0">
      <div class="news-date">16 MAR 2015</div>
      <p>Lorem ipsum dolor sit amet is consectetur adipiscing elit sed eiusmod tempor incididunt. <a href="#">Read more &raquo;</a></p>
    </div>
    <div class="news-item" style="top:82px">
      <div class="news-date">16 MAR 2015</div>
      <p>Lorem ipsum dolor sit amet is consectetur adipiscing elit sed eiusmod tempor incididunt. <a href="#">Read more &raquo;</a></p>
    </div>
    <div class="news-item" style="top:165px">
      <div class="news-date">16 MAR 2015</div>
      <p>Lorem ipsum dolor sit amet is consectetur adipiscing elit sed eiusmod tempor incididunt. <a href="#">Read more &raquo;</a></p>
    </div>
  </div>
</main>

<footer class="site-footer">
  <nav class="foot-nav"><a href="#">HOME</a><span>|</span><a href="#">OUR SERVICES</a><span>|</span><a href="#">INDUSTRY SOLUTIONS</a><span>|</span><a href="#">CONTACT US</a></nav>
  <p class="copyright">Copyright 2015 &copy; Freightora Alliance . All Rights Reserved</p>
  <div class="follow">Follow us on :</div>
  <div class="social">
    <a href="#" aria-label="Chatterpost"></a>
    <a href="#" aria-label="Circlenet"></a>
    <a href="#" aria-label="Workvine"></a>
    <a href="#" aria-label="Pinboardly"></a>
  </div>
  <div class="foot-brand"><span class="dot"></span><span>Freightora Alliance</span></div>
</footer>

</body>
</html>
```